Flyer-Design für Shop für nachhaltige Haustierprodukte
Tolle Umsetzung nach den Vorgaben. Änderungen super und schnell umgesetzt. Gerne wieder!
Zielgruppe
MELBOR ist ein Online-Marktplatz für nachhaltige Haustierprodukte. Meine Zielgruppe sind Frauen zwischen 30 und 60 Jahren mit Haustieren (Hund, Katze, Pferd)
Aufgabenstellung
Das Design soll an der Webseite angepasst sein. Es ist wichtig, dass das Thema Nachhaltigkeit kommuniziert wird und welche Vorteile MELBOR hat (Markenvielvalt, kleine Manufakturen, Handmade etc.)

```html
<!DOCTYPE html>
<html lang="de">
<head>
<meta charset="utf-8">
<title>MELBOR Flyer</title>
<link href="https://fonts.googleapis.com/css2?family=Montserrat:wght@400;500;700&display=swap" rel="stylesheet">
<style>
  :root {
    --orange: #ef7630;
    --ink: #111111;
    --grey: #4f4f4f;
    --white: #ffffff;
  }
  * { margin: 0; padding: 0; box-sizing: border-box; }
  html, body { width: 1200px; height: 2400px; overflow: hidden; background: var(--white); }
  .flyer {
    position: relative;
    width: 1200px;
    height: 2400px;
    font-family: "Montserrat", Arial, sans-serif;
    background: var(--white);
  }
  .mission {
    position: absolute;
    left: 120px;
    top: 118px;
    width: 960px;
    font-size: 44px;
    font-weight: 500;
    line-height: 56.5px;
    color: var(--ink);
  }
  .benefits { list-style: none; }
  .benefit {
    position: absolute;
    left: 120px;
    width: 1000px;
    height: 140px;
  }
  .benefit-icon {
    position: absolute;
    left: 0;
    top: 0;
    width: 140px;
    height: 140px;
  }
  .benefit-title {
    position: absolute;
    left: 198px;
    top: -2px;
    font-size: 42px;
    font-weight: 700;
    color: var(--orange);
    white-space: nowrap;
  }
  .benefit-text {
    position: absolute;
    left: 198px;
    top: 58px;
    font-size: 31px;
    font-weight: 400;
    line-height: 44px;
    color: var(--grey);
    white-space: nowrap;
    letter-spacing: 0.3px;
  }
  .photo {
    position: absolute;
    top: 1597px;
    height: 624px;
  }
  .photo-horse {
    left: 0;
    width: 477px;
    background: linear-gradient(100deg, #6b3a22 0%, #8a5534 35%, #c9b9a8 60%, #dcd6cc 100%);
  }
  .photo-cat {
    left: 477px;
    width: 723px;
    background: radial-gradient(ellipse at 50% 75%, #2a1c16 0%, #2a1c16 30%, transparent 55%),
                linear-gradient(180deg, #f0dcc0 0%, #d9a060 25%, #6d7a55 60%, #556a48 100%);
  }
  .url-band {
    position: absolute;
    left: 0;
    top: 2221px;
    width: 1200px;
    height: 179px;
    background: var(--orange);
    display: flex;
    align-items: center;
    justify-content: center;
  }
  .url {
    font-size: 60px;
    font-weight: 700;
    color: var(--white);
    letter-spacing: 0.5px;
  }
</style>
</head>
<body>
<div class="flyer">
  <p class="mission">Unsere Mission ist es, mit einer ehrlichen Online-Plattform fair und ökologisch hergestellte Haustierprodukte sichtbar zu machen. Für ein nachhaltiges Leben mit Haustier sowie einen reduzierten ökologi­schen Fußabdruck.</p>

  <ul class="benefits">
    <li class="benefit" style="top:535px">
      <svg class="benefit-icon" viewBox="0 0 140 140">
        <circle cx="70" cy="70" r="66" fill="none" stroke="var(--orange)" stroke-width="6"/>
        <path d="M28 104 C30 60 70 40 112 34 C112 80 90 108 48 104 C62 90 80 78 96 58 C76 74 58 88 36 108 Z" fill="var(--orange)"/>
      </svg>
      <h2 class="benefit-title">Fair &amp; ökologisch</h2>
      <p class="benefit-text">Geringe Umweltbelastung bei der<br>Produktion und faire Bezahlung</p>
    </li>
    <li class="benefit" style="top:735px">
      <svg class="benefit-icon" viewBox="0 0 140 140">
        <circle cx="70" cy="70" r="66" fill="none" stroke="var(--orange)" stroke-width="6"/>
        <path d="M38 32 H102 L114 56 V66 H26 V56 Z" fill="var(--orange)"/>
        <path d="M34 70 H106 V110 H82 V88 H58 V110 H34 Z" fill="var(--orange)"/>
      </svg>
      <h2 class="benefit-title">Kleine Manufakturen</h2>
      <p class="benefit-text">Viele Produkte aus kleineren<br>Manufakturen, hergestellt mit Herzblut</p>
    </li>
    <li class="benefit" style="top:935px">
      <svg class="benefit-icon" viewBox="0 0 140 140">
        <circle cx="70" cy="70" r="66" fill="none" stroke="var(--orange)" stroke-width="6"/>
        <g fill="var(--orange)">
          <rect x="52" y="42" width="10" height="42" rx="5"/>
          <rect x="64" y="32" width="10" height="52" rx="5"/>
          <rect x="76" y="36" width="10" height="48" rx="5"/>
          <rect x="88" y="46" width="10" height="40" rx="5"/>
          <path d="M52 76 H98 V92 C98 106 88 114 76 114 C64 114 56 108 48 98 L38 82 C36 76 44 72 48 78 L52 84 Z"/>
        </g>
      </svg>
      <h2 class="benefit-title">Schadstofffrei</h2>
      <p class="benefit-text">Die Produkte enthalten keine schädliche<br>Chemie oder Schadstoffe</p>
    </li>
    <li class="benefit" style="top:1135px">
      <svg class="benefit-icon" viewBox="0 0 140 140">
        <circle cx="70" cy="70" r="66" fill="none" stroke="var(--orange)" stroke-width="6"/>
        <g fill="var(--orange)">
          <path d="M20 56 L44 42 L70 52 L46 66 Z"/>
          <path d="M70 52 L96 42 L120 56 L94 66 Z"/>
          <path d="M36 68 L66 74 V108 L36 98 Z"/>
          <path d="M74 74 L104 68 V98 L74 108 Z"/>
        </g>
      </svg>
      <h2 class="benefit-title">Nachhaltig verpackt</h2>
      <p class="benefit-text">Nachhaltig Verpackt vom Packaging<br>bis hin zum Versandkarton</p>
    </li>
    <li class="benefit" style="top:1335px">
      <svg class="benefit-icon" viewBox="0 0 140 140">
        <circle cx="70" cy="70" r="66" fill="none" stroke="var(--orange)" stroke-width="6"/>
        <path d="M104 44 A34 34 0 1 0 104 96" fill="none" stroke="var(--orange)" stroke-width="14"/>
        <rect x="28" y="56" width="50" height="10" fill="var(--orange)"/>
        <rect x="28" y="74" width="50" height="10" fill="var(--orange)"/>
      </svg>
      <h2 class="benefit-title">Faire Preise</h2>
      <p class="benefit-text">Hochwertige Produkte mit<br>langer Lebensdauer zu fairen Preisen</p>
    </li>
  </ul>

  <div class="photo photo-horse" role="img" aria-label="Foto: Hand bürstet ein braunes Pferd mit einer Striegelbürste"></div>
  <div class="photo photo-cat" role="img" aria-label="Foto: Schwarze Katze hebt die Pfote vor warmem Gegenlicht im Grünen"></div>

  <div class="url-band">
    <span class="url">www.melbor.de</span>
  </div>
</div>
</body>
</html>
```